Dynamic Templates

Our company hosts web stores for our clients. They can set up as many as they wish on our platform, and select from the stock templates we provide. We are looking to increase the number of available stock templates.

Because our users can dynamically control many of the template elements - specifically colors - they have to be flexible and abide by certain rules. These rules are spelled out in the attached documents.

Here are links to two of our most used templates:
http://fernridge.vexalcart.example/
http://stampled.vexalcart.example/

Templates need to have a landing page (what you see when first clicking one of the above links). There also needs to be a category page (what you see when clicking any category) and a product detail page (what you see when you arrive at an individual product, where there are various cart options like Buy Now or Request Info).

```html
<!DOCTYPE html>
<html lang="en">
<head>
<meta charset="utf-8">
<title>BrightWare Goods – Promotional Products</title>
<link rel="stylesheet" href="https://fonts.googleapis.com/css2?family=Arimo:wght@400;700&family=Open+Sans:wght@400;600&display=swap">
<style>
:root{
  --orange:#e8570f;
  --brand-orange:#f26a1b;
  --ink:#222;
  --muted:#8a8a8a;
  --link:#555;
  --blue-btn:#1b95d0;
  --blue-btn-dark:#127bb0;
  --banner-top:#c9d8e4;
  --banner-bottom:#9fb5c6;
  --panel:#a9bccb;
  --footer-top:#e4e6e8;
  --footer-bottom:#f4f5f6;
  --dark-btn:#4a5560;
}
*{margin:0;padding:0;box-sizing:border-box}
html,body{width:1200px;height:1077px;overflow:hidden;background:#fff}
body{position:relative;font-family:"Open Sans",sans-serif;color:var(--ink)}
.abs{position:absolute}
.top-rule{left:0;top:0;width:1200px;height:7px;background:linear-gradient(#d4d4d4,#f3f3f3)}
.brand{left:100px;top:33px;display:flex;align-items:center;gap:12px}
.brand-mark{width:46px;height:46px;border-radius:50%;background:var(--brand-orange)}
.brand-name{font-family:"Arimo",sans-serif;font-weight:700;font-size:21px;color:var(--brand-orange)}
.search-field{border:1px solid #d5d5d5;background:#fff}
.btn-blue{background:linear-gradient(var(--blue-btn),var(--blue-btn-dark));color:#fff;font-family:"Arimo",sans-serif;font-size:12px;letter-spacing:.5px;display:flex;align-items:center;justify-content:center}
.nav-rule{left:0;top:120px;width:1200px;height:1px;background:linear-gradient(90deg,transparent,#e6e6e6 20%,#e6e6e6 80%,transparent)}
.nav a{position:absolute;top:92px;height:48px;display:flex;align-items:center;justify-content:center;font-family:"Arimo",sans-serif;font-weight:700;font-size:14px;color:#555;text-decoration:none;background:linear-gradient(#d9d9d9,#f7f7f7 35%,#fff)}
.banner{left:0;top:144px;width:1200px;height:318px;background:linear-gradient(var(--banner-top),var(--banner-bottom))}
.cats{left:102px;top:144px;width:142px;height:318px}
.cats h3{height:31px;padding:8px 5px;font-family:"Arimo",sans-serif;font-size:13px;font-weight:700;color:#222;background:#dbe5ec}
.cats ul{list-style:none;padding:7px 0 0 6px}
.cats li{font-family:"Arimo",sans-serif;font-size:11px;color:#fff;height:21px;line-height:17px}
.stage{left:244px;top:144px;width:694px;height:318px;background:linear-gradient(#e9eef2,#d4dde4 70%,#b8c6d2)}
.seller-panel{left:938px;top:144px;width:262px;height:318px;background:linear-gradient(#b6c9d8,#9fb5c6)}
.seller-title{left:965px;top:182px;font-family:"Arimo",sans-serif;font-weight:700;font-size:12px}
.seller-box{left:953px;top:206px;width:145px;height:210px;background:#b1c0cc}
.seller-name{left:965px;top:211px;width:125px;font-family:"Arimo",sans-serif;font-weight:700;font-size:12px;line-height:19px;color:#fff}
.seller-photo{left:953px;top:254px;width:145px;height:107px;background:radial-gradient(circle at 50% 50%,#d6303a 0 26%,#fbfbfb 30%)}
.price{left:953px;top:366px;width:145px;text-align:center;font-family:"Arimo",sans-serif;font-weight:700;font-size:12px;color:#fff}
.btn-dark{background:var(--dark-btn);color:#fff;font-family:"Arimo",sans-serif;font-weight:700;font-size:12px;display:flex;align-items:center;justify-content:center;gap:6px;border:1px solid #7b8791}
.under-band{left:0;top:462px;width:1200px;height:9px;background:#e9ecee}
.intro h2{position:absolute;left:107px;font-size:18px;font-weight:400;color:var(--orange)}
.intro p{position:absolute;left:109px;width:990px;font-size:12.5px;line-height:21px;color:var(--muted);letter-spacing:.2px}
.footer{left:0;top:708px;width:1200px;height:306px;border-top:2px solid #eee;background:linear-gradient(var(--footer-top),var(--footer-bottom))}
.foot-h{font-size:18px;font-weight:400}
.foot-list{list-style:none;font-size:12.5px;color:var(--link);letter-spacing:.3px}
.foot-list li{height:21px}
.vdots{width:0;border-left:1px dotted #777}
.contact-box{left:834px;top:809px;width:265px;height:191px;background:#fafafa;border:1px solid #dcdcdc}
.field-label{font-size:11px;color:#333;text-align:right;width:95px}
.field{width:154px;height:18px;border:1px solid #ccc;background:#fff}
.contact-link{left:883px;font-size:12.5px;color:var(--orange)}
.bottom-rule{left:0;top:1014px;width:1200px;border-top:1px dotted #999}
.copyright{left:0;top:1031px;width:1200px;text-align:center;font-family:"Arimo",sans-serif;font-size:12px;color:#666}
</style>
</head>
<body>
<div class="abs top-rule"></div>

<header>
  <div class="abs brand"><span class="brand-mark"></span><span class="brand-name">BrightWare Goods</span></div>
  <div class="abs search-field" style="left:825px;top:28px;width:185px;height:23px"></div>
  <div class="abs btn-blue" style="left:1018px;top:29px;width:79px;height:21px">SEARCH</div>
  <div class="abs nav-rule"></div>
  <nav class="nav">
    <a style="left:326px;width:84px">HOME</a>
    <a style="left:420px;width:95px">ABOUT US</a>
    <a style="left:525px;width:95px">PRODUCTS</a>
    <a style="left:630px;width:103px">CONTACT US</a>
    <a style="left:743px;width:130px">HOW TO ORDER</a>
  </nav>
</header>

<section class="abs banner"></section>
<aside class="abs cats">
  <h3>TOP CATEGORIES</h3>
  <ul>
    <li>APPAREL</li><li>BAGS TOTES</li><li>CAPS HATS</li><li>COMPUTER</li><li>ECO FRIENDLY</li>
    <li>FOOD, CANDY DRINK</li><li>HOME HOUSEWARES</li><li>KEYCHAINS</li><li>NOTEBOOKS FOLIOS</li>
    <li>BUSINESS SUPPLIES</li><li>NOTEBOOKS FOLIOS</li><li>TOOLS HARDWARE</li><li>WRITING INSTRUMENTS</li>
  </ul>
</aside>
<div class="abs stage" role="img" aria-label="Product carousel showing a featured desk puzzle award with smaller promotional items fanned to either side"></div>

<aside>
  <div class="abs seller-panel"></div>
  <div class="abs seller-title">TOP SELLER</div>
  <div class="abs seller-box"></div>
  <div class="abs seller-name">Ridgeline Corporate Fill - Blue</div>
  <div class="abs seller-photo" role="img" aria-label="Red spiral-bound notebook with pen"></div>
  <div class="abs price">$ 19.99</div>
  <div class="abs btn-dark" style="left:979px;top:390px;width:93px;height:20px">Info <span>/</span> Buy</div>
  <div class="abs btn-dark" style="left:953px;top:429px;width:145px;height:20px;font-weight:400;font-size:13px">
    <svg width="20" height="14" viewBox="0 0 20 14"><path d="M1 1h3l2 8h10l2-6H5" fill="none" stroke="#fff" stroke-width="1.5"/><circle cx="8" cy="12" r="1.5" fill="#fff"/><circle cx="15" cy="12" r="1.5" fill="#fff"/></svg>
    START SHOPPING</div>
</aside>

<div class="abs under-band"></div>

<main class="intro">
  <h2 style="top:483px">Welcome To The Future of Promotional Products!</h2>
  <p style="top:515px">Gone are the days of searching through dog-eared catalogs or trying to make sense of complicated product websites.</p>
  <p style="top:557px">We do the work for you! We've taken only the very best and most current products and placed them in easy-to-use categories designed for your needs. Take a look at our selection - quality products at excellent prices.</p>
  <h2 style="top:611px">Enjoy This Amazing New Resource</h2>
  <p style="top:644px">We know you don't have time to waste; so we've cut to the chase and made it simple! But keep in mind, we do have access to over a million products - so if you don't see what you're looking for or have a special theme or request, let us know - we'll find it!</p>
</main>

<footer>
  <div class="abs footer"></div>
  <h3 class="abs foot-h" style="left:107px;top:729px;color:var(--orange)">Shop By Category</h3>
  <ul class="abs foot-list" style="left:109px;top:764px">
    <li>Apparel</li><li>Auto</li><li>Awards &amp; Recognition</li><li>Bags &amp; Totes</li><li>Business Supplies</li><li>Calendars,</li><li>Books &amp; Cards</li><li>Caps &amp; Hats</li><li>Clocks &amp; Watches</li><li>Company Outings</li><li>Computer</li>
  </ul>
  <ul class="abs foot-list" style="left:285px;top:766px">
    <li>Desktop &amp; Office</li><li>Eco Friendly</li><li>Electronics</li><li>Executive Gifts</li><li>Food, Candy &amp; Drink</li><li>Games &amp; Novelties</li><li>Gift Sets</li><li>Golf, Sports &amp; Outdoors</li><li>Healthcare &amp; Safety</li><li>Writing Instruments</li><li>Corporate Gifts</li>
  </ul>
  <ul class="abs foot-list" style="left:472px;top:762px">
    <li>Holiday</li><li>Home &amp; Housewares</li><li>Keychains</li><li>Mugs &amp; Drin</li><li>kware</li><li>Notebooks &amp; Folios</li><li>Pocket &amp; Purse</li><li>Stress Balls &amp; Relievers</li><li>Tools &amp; Hardware</li><li>Tradeshows &amp; Events</li><li>Travel &amp; Luggage</li>
  </ul>
  <div class="abs vdots" style="left:649px;top:765px;height:234px"></div>
  <h3 class="abs foot-h" style="left:668px;top:729px;color:#333">Shop By Price</h3>
  <ul class="abs foot-list" style="left:677px;top:768px">
    <li>Under $5</li><li>$5 - $10</li><li>$10 - $20</li><li>$20 - $50</li><li>$50 - $100</li><li>$100 - $200</li><li>Over $200</li>
  </ul>
  <div class="abs vdots" style="left:827px;top:765px;height:234px"></div>
  <h3 class="abs foot-h" style="left:879px;top:730px;color:#333">Quick Search</h3>
  <div class="abs search-field" style="left:847px;top:770px;width:168px;height:22px"></div>
  <div class="abs btn-blue" style="left:1019px;top:770px;width:63px;height:21px">SEARCH</div>
  <div class="abs contact-box"></div>
  <h3 class="abs foot-h" style="left:885px;top:815px;color:#333">Contact Us</h3>
  <div class="abs field-label" style="left:830px;top:851px">Name</div>
  <div class="abs field" style="left:936px;top:849px"></div>
  <div class="abs field-label" style="left:830px;top:881px">Phone Number</div>
  <div class="abs field" style="left:936px;top:879px"></div>
  <div class="abs field-label" style="left:830px;top:911px">Email</div>
  <div class="abs field" style="left:936px;top:909px"></div>
  <div class="abs btn-blue" style="left:1036px;top:934px;width:51px;height:21px;font-size:13px">GO</div>
  <div class="abs contact-link" style="top:957px">info@brightwaregoods.example</div>
  <div class="abs contact-link" style="top:976px">www.brightwaregoods.example</div>
  <div class="abs bottom-rule"></div>
  <div class="abs copyright">Copyright © 2010 . BrightWareGoods.example V3 . All Rights Reserved.</div>
</footer>
</body>
</html>
```